Grain Roll Package Re-Design (Food)

Attached is our current package design. We need complete re-design of our current package. Here are changes needed:

1) Product name:
Product name doesn't catch consumer's eyes. Product name itself must stand out. By looking at the product name, consumer must get an idea of what this product is.
Also, product name needs to be changed to 'Crispy Field Harvest Nuggets'.

Also the main feature of this product is that it is made of 21 Multi Grains. So this must be reflected clearly on the package! Without reading the package, consumer must clearly understand that this product is made of 21 Multi Grains therefore, it is a healthy snack, great replacement for meals.

2) Product actual size picture:
On the front side of the package, there must be an actual size of the product.

3) Net Weight
Needs to be 2.82 oz (80g)

4) Velto logo needs to be changed to the new uploaded one (with grandma face).

5) Sorvane, Inc logo attached (Manufactured exclusively for Sorvane, Inc.)

6) Example package we liked were
www.plumvikesnacks.com (simple but powerful, clean and clearly tells what the product is)
www.torelliusa.com
Odette Brill's food
Wendle Puffed Wafers

Current package AI file is on the following dropbox:

https://www.filevaultexample.net/sh/kq7rm2tz91wx/ZZq4LmTnRbVcXeWpYdHsJuAo3?dl=0

Actual Product Image:
I've uploaded on my product page.

Our current package design needs to be completely changed into new design.

Hi I've uploaded both AI and PDF files of product actual image. Please put the actual product image. You don't have to put the exact same image (whether you put one roll image or whole group, I will leave up to the designer. Be creative!). Thanks.

Thank you for your participation in our project. Due to the production issue, we will need only one flavor (Cheese). We reviewed all of designs you have submitted and we felt there were many great designs. However, we felt none of design has reflected the feature of 21 grain. The main essential feature of this product is that it is made of 21 Multi Grains, and this point should be emphasized. This is the main feature that differentiates our product from others. This product is a healthy snack, and it can be a great meal replacement since it is made of 21 multi grains.

I will need only one design (I won't need Green Tea, Strawberry, Chocolate flavors). So I will need one design for one product (Crispy Field Harvest Nuggets). I showed all of your design drafts to my buyers. Buyers have commented that the none of the packages reflect or show that this product is made of 21 kind of multi grains. This is the very crucial important factor. I need a design that shows the product is made of multi grains so healthy snack. You can use my old existing design I've uploaded.

Target Market(s)

Mothers, LOHAS consumers, Millenials, Foodies

Industry/Entity Type

Food Production

Requirements
Must have
• 21 Multi Grain must be clearly and strongly emphasized on the package. This product is a special, healthy and unique snack because it is made of 21 kinds of Multi Grains!
Nice to have
• COLORFUL, CONSISTENCY
• I'VE UPLOADED THE OTHER COMPANIES' PACKAGES I LIKED
• http://www.quandelfare.com/products

```html
<!DOCTYPE html>
<html lang="en">
<head>
<meta charset="utf-8">
<title>Crispy Field Harvest Nuggets – Pouch Front</title>
<link rel="stylesheet" href="https://fonts.googleapis.com/css2?family=Amatic+SC:wght@400;700&family=Caveat:wght@700&family=Kaushan+Script&display=swap">
<style>
  :root {
    --stage: #7b98a4;
    --pouch-yellow: #efc15f;
    --pouch-yellow-light: #f6d483;
    --panel-white: #ffffff;
    --title-orange: #e58a1c;
    --title-brown: #3a2114;
    --accent-red: #b8283a;
    --logo-red: #a8232c;
    --badge-green: #4f8a4a;
    --badge-olive: #7f9a3c;
    --badge-sage: #5e8a6a;
    --snack-tan: #d9975a;
    --snack-light: #efc99a;
    --ink-soft: #4a3a30;
  }
  * { box-sizing: border-box; margin: 0; padding: 0; }
  html, body { width: 1200px; height: 1190px; overflow: hidden; }
  body { background: var(--stage); position: relative; font-family: "Amatic SC", sans-serif; }

  .pouch {
    position: absolute; left: 318px; top: 129px; width: 564px; height: 932px;
    border-radius: 10px 10px 14px 14px; overflow: hidden;
  }
  .pouch__pattern {
    position: absolute; inset: 0;
    background: radial-gradient(ellipse at 50% 40%, var(--pouch-yellow-light), var(--pouch-yellow) 70%);
  }
  .pouch__zip {
    position: absolute; left: 0; right: 0; top: 104px; height: 2px;
    background: rgba(0,0,0,0.06);
  }
  .label {
    position: absolute; left: 90px; top: 0; width: 382px; height: 877px;
    background: var(--panel-white);
  }

  .brand {
    position: absolute; left: 0; right: 0; top: 50px;
    display: flex; justify-content: center; align-items: center; gap: 10px;
  }
  .brand__dot { width: 22px; height: 22px; border-radius: 50%; background: var(--logo-red); }
  .brand__name {
    font-family: "Kaushan Script", cursive; font-size: 40px; color: var(--logo-red); line-height: 1;
  }

  .title { position: absolute; left: 0; right: 0; top: 132px; text-align: center; }
  .title__lead {
    display: block; font-family: "Caveat", cursive; font-weight: 700;
    font-size: 52px; line-height: 1; color: var(--title-brown);
  }
  .title__main {
    display: block; font-family: "Amatic SC", sans-serif; font-weight: 700;
    font-size: 128px; line-height: 0.92; color: var(--title-orange); margin-top: 6px;
  }
  .title__sub {
    display: block; font-family: "Amatic SC", sans-serif; font-weight: 700;
    font-size: 118px; line-height: 0.92; color: var(--title-brown);
  }

  .side-claim {
    position: absolute; left: 8px; top: 226px; width: 600px; height: 34px;
    transform-origin: 0 0; transform: translate(34px, 0) rotate(90deg);
    font-family: "Amatic SC", sans-serif; font-weight: 700; font-size: 25px;
    color: var(--ink-soft); letter-spacing: 1px; white-space: nowrap; line-height: 34px;
  }
  .side-claim__em {
    font-family: "Caveat", cursive; font-weight: 700; font-size: 34px;
    color: var(--title-orange); margin: 0 4px;
  }

  .filling-note {
    position: absolute; left: 150px; top: 432px; width: 190px;
    font-family: "Caveat", cursive; font-weight: 700; font-size: 34px; line-height: 0.95;
    color: var(--accent-red); text-align: center; transform: rotate(-7deg);
  }
  .arrows { position: absolute; left: 0; top: 440px; width: 382px; height: 220px; }

  .product-shot {
    position: absolute; left: 58px; top: 580px; width: 280px; height: 215px;
    border-radius: 48% 52% 46% 54%;
    background: radial-gradient(circle at 50% 45%, var(--snack-light), var(--snack-tan) 75%, rgba(217,151,90,0) 100%);
  }

  .net-weight {
    position: absolute; left: 30px; top: 810px;
    font-family: "Amatic SC", sans-serif; font-weight: 700; font-size: 26px; color: var(--ink-soft);
    white-space: nowrap;
  }
  .badges { position: absolute; left: 170px; top: 810px; display: flex; gap: 16px; }
  .badge { width: 48px; height: 48px; border-radius: 50%; }
  .badge--one { background: var(--badge-green); }
  .badge--two { background: var(--badge-olive); }
  .badge--three { background: var(--badge-sage); }
</style>
</head>
<body>
  <div class="pouch">
    <div class="pouch__pattern" role="img" aria-label="Yellow Swiss cheese texture with scattered holes"></div>
    <div class="pouch__zip"></div>

    <div class="label">
      <div class="brand">
        <span class="brand__dot"></span>
        <span class="brand__name">Velto</span>
      </div>

      <h1 class="title">
        <span class="title__lead">Crispy Field</span>
        <span class="title__main">HARVEST</span>
        <span class="title__sub">NUGGETS</span>
      </h1>

      <p class="side-claim">ENJOY TEH GOODNESS OF <span class="side-claim__em">21 Grains</span> IN DELICIOUS MINI BITES</p>

      <p class="filling-note">filled with soft cream cheese</p>

      <svg class="arrows" viewBox="0 0 382 220" aria-hidden="true">
        <g fill="none" stroke="var(--accent-red)" stroke-width="2.5" stroke-linecap="round" stroke-linejoin="round">
          <path d="M140 20 C 100 32, 82 80, 92 128"/>
          <path d="M80 115 L92 130 L102 113"/>
          <path d="M332 92 C 354 112, 354 142, 338 164"/>
          <path d="M332 148 L337 166 L352 158"/>
        </g>
      </svg>

      <div class="product-shot" role="img" aria-label="Pile of baked grain roll bites filled with cream cheese"></div>

      <p class="net-weight">80 g / 2.82 oz</p>

      <div class="badges">
        <span class="badge badge--one"></span>
        <span class="badge badge--two"></span>
        <span class="badge badge--three"></span>
      </div>
    </div>
  </div>
</body>
</html>
```